The Little Meadow Biscuit Bakery Swing Tag Label Design/Logo

Hi! We are looking for a “swing tag” label design for our different flavoured packs of (6) cookies. Basic info on the front (business name “The Little Meadow Biscuit Bakery”, strap line being “Handmade Gourmet Cookies” (not made in Norfolk) and the flavour “Choc Chip”, “Original”, “Choc Orange”, etc…).
The flavour part of the label being colour coded to suit, so dark brown for choc chip, beige for original, orange for choc orange, red/white for cranberry & white choc, bla bla bla!!
The rear of the tag to display ingredients, barcode, business postcode, suitable for Vegans, Dairy Free, Fenwick Approved Logo and Net Weight 300g.
Packaging is clear cellophane bags, with crimp seal. Three cookies stacked side by side with a brown Jute string tied around the packaging which will hold the tag.
We are selling in farm shops, deli’s and local food stores, so want to have a modern/smart feel to the design, yet retain the appeal of a small “cottage industry/countryside” style business.
The attached image is where we have got so far (with our very basic design skills) , but do not let this guide you too much, as we are looking for inspiration. (Appreciate the attached does not have the cottage/country appeal)!!
Size is undetermined, but thinking 100mm x 50mm, ish? Not ruled out a round label either, being cookies?
Labels will also be the basis for our business cards, internet pages (facebook, Instagram, etc…), so the design wants to be catchy, instantly recognisable and “say what it does on the tin”.
We also have single pack cookies in cellophane bags, so would be great if the deign could be printed in sticky label format also.
Not decided if the labels will be “craft paper” brown tags, or white, or another colour. Open to suggestions.
Like the idea of the “bite” out of the cookie, but needs “some teeth” if you get what I mean.
Feel free to message if you wish!
Thanks for your time.

Logo Text

The Little Meadow Biscuit Bakery or THE LITTLE MEADOW BISCUIT BAKERY

```html
<!DOCTYPE html>
<html lang="en">
<head>
<meta charset="utf-8">
<title>The Little Meadow Biscuit Bakery – Flavour Labels</title>
<link href="https://fonts.googleapis.com/css2?family=Londrina+Solid:wght@400;900&display=swap" rel="stylesheet">
<style>
  :root {
    --ink: #000000;
    --paper: #ffffff;
    --canvas-edge: #9a9a9a;
    --flavour-orange: #ff6600;
    --flavour-original: #cc9933;
    --badge-text: #ffffff;
  }
  * { margin: 0; padding: 0; box-sizing: border-box; }
  html, body {
    width: 1200px;
    height: 1200px;
    overflow: hidden;
    background: var(--paper);
  }
  .sheet {
    position: relative;
    width: 1200px;
    height: 1200px;
    border: 1px solid var(--canvas-edge);
    font-family: "Londrina Solid", "Arial Black", sans-serif;
    color: var(--ink);
  }
  .label {
    position: absolute;
    left: 212px;
    width: 798px;
    height: 436px;
    border: 10px solid var(--ink);
    border-radius: 42px;
    background: var(--paper);
  }
  .label--choc-orange { top: 83px; }
  .label--original { top: 663px; }

  .brand-name {
    position: absolute;
    right: 46px;
    top: 40px;
    text-align: right;
    font-weight: 900;
    text-transform: uppercase;
    line-height: 0.9;
    letter-spacing: 1px;
  }
  .brand-name__line {
    display: block;
    font-size: 78px;
  }
  .brand-name__line + .brand-name__line { margin-top: 6px; }

  .flavour-badge {
    position: absolute;
    left: 55px;
    top: 245px;
    width: 144px;
    height: 144px;
  }
  .flavour-badge svg { display: block; width: 100%; height: 100%; }
  .flavour-badge__name {
    position: absolute;
    inset: 0;
    display: flex;
    align-items: center;
    justify-content: center;
    text-align: center;
    color: var(--badge-text);
    font-weight: 900;
    font-size: 27px;
    line-height: 1.05;
    text-transform: uppercase;
    letter-spacing: 0.5px;
  }
  .label--original .flavour-badge__name { font-size: 24px; }

  .strapline {
    position: absolute;
    right: 38px;
    bottom: 28px;
    font-weight: 900;
    font-size: 40px;
    text-transform: uppercase;
    letter-spacing: 1px;
    line-height: 1;
    white-space: nowrap;
  }
</style>
</head>
<body>
  <main class="sheet">

    <section class="label label--choc-orange">
      <h1 class="brand-name">
        <span class="brand-name__line">The Little Meadow</span>
        <span class="brand-name__line">Biscuit Bakery</span>
      </h1>
      <div class="flavour-badge">
        <svg viewBox="0 0 144 144" aria-hidden="true">
          <circle cx="72" cy="72" r="72" fill="var(--flavour-orange)"/>
        </svg>
        <p class="flavour-badge__name">Choc<br>Orange</p>
      </div>
      <p class="strapline">Handmade Gourmet Cookies</p>
    </section>

    <section class="label label--original">
      <h2 class="brand-name">
        <span class="brand-name__line">The Little Meadow</span>
        <span class="brand-name__line">Biscuit Bakery</span>
      </h2>
      <div class="flavour-badge">
        <svg viewBox="0 0 144 144" aria-hidden="true">
          <circle cx="72" cy="72" r="72" fill="var(--flavour-original)"/>
        </svg>
        <p class="flavour-badge__name">Original</p>
      </div>
      <p class="strapline">Handmade Gourmet Cookies</p>
    </section>

  </main>
</body>
</html>
```